Kestavo Estates is a commercial real estate development company based in the United States. We develop high-end office buildings and student housing apartments. We have a new logo and need to update all of our stationary items and business cards. We would like the design to be clean and professional. Our logo and color information is attached. Our logo MUST be in full color and not as white. It is preferred that the logo is on a white background.

Color code Blue R 0. G 62. B 124 ( #003E7C )
C 100 M84 Y 26 K 22
Black R32. G30. B30 ( #201E1E)
C100 M100 Y100 K100

Font used TRAJAN PRO3 PRO BOLD.

Items needed:
1. Business card - Leaning towards doing just a one side business card in a thicker paper. Include - logo, name - Peter T. Vance, Title - Chairman & CEO, 1870 Pembrook Blvd. Suite 400, Atlanta, GA 30127 - Cell number 404.555.####, Office 770.555.02## email@kestavoestates.com; www.kestavoestates.com.

2. Letterhead - Standard 8.5 by 11 paper. We do have a smaller size for the CEO that is 7.25 by 10.5 that is just a mirror of the letterhead except with his name (Peter T. Vance) and title (Chariman & CEO) listed at the top in the header. Letthead needs address, phone number and website, plus logo. *Prepared such that we can either implement as a Google Document template or professionally print.

3. Legal sized envelope - #10 envelope - which measures 4 1/8" by 9 1/2". We also use the same size envelope with a window. Need logo and address. A photo of the old envelope style is attached.

4. 9" x 12" Pocket folder - Need a design that can also be split to be a cover page and back - We use the cover pages in spiral binding machine, so we need to leave room on the left for that. One of the pockets should hold a business card. Include logo, address, phone, website. Also if text is needed, we could say development / leasing / property management.

5. Shipping label - 3 1/3" x 4" inches and 6 per page. Just need logo and address listed at top of the label and white space at bottom.

Company: Kestavo Estates
Address: 1870 Pembrook Blvd. Suite 400, Atlanta, GA 30127
Phone: 770.555.0214
Fax: 770.555.0287 (probably not needed)
Website: www.kestavoestates.com

Thank you for all your help!

Target Market(s)

Should communicate a strong corporate feel

Contact Information for Business Card

Include - logo, name - Peter T. Vance, Title - Chairman & CEO, 1870 Pembrook Blvd. Suite 400, Atlanta, GA 30127 - Cell number 404.555.####, Office 770.555.02## email@kestavoestates.com; www.kestavoestates.com.

Logo Text

Kestavo Estates

Colors

Requirements
Must have
• Our logo MUST be in full color and not as white. It is preferred that the logo is on a white background.
• Colors - Color code Blue R 0. G 62. B 124 ( #003E7C )
• C 100 M84 Y 26 K 22
Nice to have
• Font used in logo TRAJAN PRO3 PRO BOLD. Would love to see options of both a one sided and double-sided.
Should not have
• Logo in white.

```html
<!DOCTYPE html>
<html lang="en">
<head>
<meta charset="utf-8">
<title>Kestavo Estates — Stationery System</title>
<link href="https://fonts.googleapis.com/css2?family=Cinzel:wght@700&family=Open+Sans:ital,wght@0,400;0,600;0,700;1,400&display=swap" rel="stylesheet">
<style>
  :root{
    --brand-blue:#003E7C;
    --ink:#201E1E;
    --paper:#ffffff;
    --board:#d9d9d9;
    --caption:#2a4a7a;
    --faint:#eef0f3;
    --rule:#9aa3ae;
  }
  *{box-sizing:border-box;margin:0;padding:0}
  html,body{width:1200px;height:902px;overflow:hidden}
  body{background:var(--board);position:relative;font-family:"Open Sans",Arial,sans-serif;color:var(--ink)}
  .sheet{position:absolute;background:var(--paper);box-shadow:0 1px 3px rgba(0,0,0,.18)}
  .caption{position:absolute;font-size:8px;font-weight:600;color:var(--caption);transform:translateX(-50%);white-space:nowrap}

  /* brand lockup: plain circle + name in one colour, one weight */
  .brand{position:absolute;display:flex;align-items:center;gap:4px;color:var(--brand-blue);font-family:"Cinzel",Georgia,serif;font-weight:700;line-height:1}
  .brand .dot{border-radius:50%;background:var(--brand-blue);flex:none}
  .brand .name{display:flex;flex-direction:column;letter-spacing:.06em}
  .brand--xs{font-size:8px}.brand--xs .dot{width:14px;height:14px}
  .brand--sm{font-size:10px}.brand--sm .dot{width:18px;height:18px}
  .brand--md{font-size:13px}.brand--md .dot{width:24px;height:24px}

  /* business card */
  .card{width:188px;height:107px;top:89px}
  .card .divider{position:absolute;left:102px;top:30px;width:1px;height:46px;background:var(--rule)}
  .card .contact{position:absolute;left:110px;top:30px;font-size:5px;line-height:1.35;color:var(--ink)}
  .card .contact .person{font-size:6.4px;font-weight:700;color:var(--brand-blue)}
  .card .contact .role{font-size:4.6px;font-weight:600;margin-bottom:4px}
  .card .contact b{font-weight:700}
  .card .contact .gap{height:4px}

  /* letterhead */
  .letterhead{width:276px;height:390px;top:250px}
  .letterhead .header-contact{position:absolute;left:185px;top:40px;font-size:5px;line-height:1.4;border-left:1px solid var(--rule);padding-left:5px}
  .letterhead .letter{position:absolute;left:19px;top:127px;width:240px;font-size:4.2px;line-height:1.55;color:#555}
  .letterhead .salutation{font-size:7px;color:var(--ink);margin-bottom:10px}
  .letterhead .letter p{margin-bottom:6px;text-align:justify}
  .letterhead .signoff{margin-top:8px;font-size:4.4px}

  /* envelope */
  .env-back{width:275px;height:124px;top:674px;background:#f4f4f4}
  .env-back .flap{position:absolute;inset:0 0 auto 0;height:50px;border-bottom:1px solid #ddd;border-radius:0 0 22px 22px;background:var(--paper)}
  .env-back .seal{position:absolute;left:50%;top:18px;width:14px;height:14px;margin-left:-7px;border-radius:50%;background:var(--brand-blue)}
  .env-front{width:276px;height:125px;top:744px}
  .env-front .window{position:absolute;left:17px;top:54px;width:76px;height:26px;border:1px solid #c9c9c9;border-radius:2px;background:linear-gradient(#eaeaea,#f6f6f6)}

  .label{left:739px;top:737px;width:155px;height:127px}

  /* pocket folder, shown flat */
  .folder-panel{width:200px;height:267px}
  .folder-back .emblem{position:absolute;left:30px;top:55px;width:140px;height:140px;border-radius:50%;background:var(--faint)}
  .folder-back .contact{position:absolute;left:14px;bottom:14px;font-size:4.6px;line-height:1.4;color:var(--ink)}
  .folder-spine{position:absolute;width:1px;background:#e2e2e2}
  .pocket{position:absolute;left:0;right:0;bottom:0;height:92px;background:#f7f7f7;border-top:1px solid #dedede;box-shadow:0 -2px 4px rgba(0,0,0,.05)}
  .pocket .tagline{position:absolute;right:14px;bottom:20px;font-size:6px;font-style:italic;color:#7c8aa3;letter-spacing:.04em}
  .card-slot{position:absolute;width:8px;height:1px;background:#9a9a9a}
</style>
</head>
<body>

  <!-- Business card: front with contact details -->
  <section class="sheet card" style="left:129px" aria-label="Business card, contact side">
    <div class="brand brand--xs" style="left:12px;top:40px"><span class="dot"></span><span class="name"><span>Kestavo</span><span>Estates</span></span></div>
    <div class="divider"></div>
    <div class="contact">
      <div class="person">PETER T. VANCE</div>
      <div class="role">CHAIRMAN &amp; CEO</div>
      <div>Office <b>770.555.0214</b></div>
      <div>Cell <b>404.555.0196</b></div>
      <div class="gap"></div>
      <div><b>email@kestavoestates.com</b></div>
      <div><b>www.kestavoestates.com</b></div>
    </div>
  </section>

  <!-- Business card: logo side -->
  <section class="sheet card" style="left:336px" aria-label="Business card, brand side">
    <div class="brand brand--md" style="left:30px;top:36px"><span class="dot"></span><span class="name"><span>Kestavo</span><span>Estates</span></span></div>
  </section>
  <div class="caption" style="left:325px;top:212px">Card</div>

  <!-- Letterhead -->
  <section class="sheet letterhead" style="left:35px" aria-label="Letterhead A4">
    <div class="brand brand--sm" style="left:19px;top:38px"><span class="dot"></span><span class="name"><span>Kestavo</span><span>Estates</span></span></div>
    <div class="header-contact">
      <div>Office <b>770.555.0214</b></div>
      <div><b>www.kestavoestates.com</b></div>
    </div>
    <div class="letter">
      <div class="salutation">Dear Mr. Ellery,</div>
      <p>Thank you for meeting with our team last week. We are pleased to share the enclosed proposal for the new office campus and look forward to your review of the attached site plans and schedules.</p>
      <p>Our leasing group has prepared updated terms for the student housing phase, including unit mix, amenity spaces and parking counts. Please note the revised dates for the second review meeting.</p>
      <p>Construction pricing remains on track, and the design team will issue final drawings next month. We will coordinate closely with your staff on permits, inspections and tenant improvements.</p>
      <p>Should you have any questions, please contact our office at your convenience.</p>
      <div class="signoff">Sincerely,</div>
    </div>
  </section>
  <div class="caption" style="left:173px;top:648px">Letterhead A4</div>

  <!-- Letterhead continuation page -->
  <section class="sheet letterhead" style="left:342px" aria-label="Letterhead A4 continuous page">
    <div class="brand brand--sm" style="left:19px;top:38px"><span class="dot"></span><span class="name"><span>Kestavo</span><span>Estates</span></span></div>
  </section>
  <div class="caption" style="left:488px;top:648px">Letterhead A4 Continuous Page</div>

  <!-- Envelope, plain -->
  <div class="sheet env-back" style="left:58px" aria-hidden="true"><div class="flap"></div><div class="seal"></div></div>
  <section class="sheet env-front" style="left:35px" aria-label="Envelope">
    <div class="brand brand--xs" style="left:17px;top:16px"><span class="dot"></span><span class="name"><span>Kestavo</span><span>Estates</span></span></div>
  </section>
  <div class="caption" style="left:179px;top:877px">Envelope</div>

  <!-- Envelope, window -->
  <div class="sheet env-back" style="left:409px" aria-hidden="true"><div class="flap"></div><div class="seal"></div></div>
  <section class="sheet env-front" style="left:385px" aria-label="Window envelope">
    <div class="brand brand--xs" style="left:17px;top:16px"><span class="dot"></span><span class="name"><span>Kestavo</span><span>Estates</span></span></div>
    <div class="window"></div>
  </section>
  <div class="caption" style="left:531px;top:877px">Envelope</div>

  <!-- Shipping label -->
  <section class="sheet label" aria-label="Shipping label">
    <div class="brand brand--xs" style="left:12px;top:15px"><span class="dot"></span><span class="name"><span>Kestavo</span><span>Estates</span></span></div>
  </section>
  <div class="caption" style="left:816px;top:870px">Shipping label</div>

  <!-- Pocket folder: outside spread (back + front) -->
  <section class="sheet folder-panel folder-back" style="left:700px;top:40px" aria-label="Pocket folder back cover">
    <div class="emblem"></div>
    <div class="contact">
      <div>Office <b>770.555.0214</b></div>
      <div><b>www.kestavoestates.com</b></div>
    </div>
  </section>
  <section class="sheet folder-panel" style="left:902px;top:40px" aria-label="Pocket folder front cover">
    <div class="brand brand--md" style="left:38px;top:110px"><span class="dot"></span><span class="name"><span>Kestavo</span><span>Estates</span></span></div>
  </section>

  <!-- Pocket folder: closed cover and inside pocket -->
  <section class="sheet folder-panel" style="left:680px;top:360px" aria-label="Pocket folder cover">
    <div class="brand brand--md" style="left:38px;top:110px"><span class="dot"></span><span class="name"><span>Kestavo</span><span>Estates</span></span></div>
  </section>
  <section class="sheet folder-panel" style="left:900px;top:360px" aria-label="Pocket folder inside with pocket">
    <div class="pocket">
      <span class="card-slot" style="left:24px;top:14px"></span>
      <span class="card-slot" style="left:24px;top:44px"></span>
      <div class="tagline">development / leasing / property management</div>
    </div>
  </section>

</body>
</html>
```